Design a blog page showing lists of latest posts.

I want to design my blog home page. This page will show a list of my latest blog posts.

The site URL is lumbero.com and I have already given a basic structure to it. Please visit and have a look at it.

The color scheme of the design should be black (or grey) and white.

Below the top header I want an opt-in form and below that list of my blog posts. Then pagination and then a bottom section, that will show my two products. Please design these two boxes without any image.

Please avoid using any background image. If necessary, use any image without a character or person. Avoid using the sidebar.

Make it beautiful with the use of typography and white spaces.

I am open to any new creative ideas. Let me know if you have any?

1 page

• Sidebar

```html
<!DOCTYPE html>
<html lang="en">
<head>
<meta charset="utf-8">
<title>Lumbero – Blog</title>
<link href="https://fonts.googleapis.com/css2?family=Jost:wght@400;500;600&family=Questrial&display=swap" rel="stylesheet">
<style>
:root{
  --ink:#231f20;
  --text:#333;
  --muted:#8a8a8a;
  --line:#cfcfcf;
  --paper:#ffffff;
  --soft:#f7f7f7;
  --placeholder:#ececec;
  --placeholder-mark:#cdcdcd;
  --band:#7f7f7f;
}
*{box-sizing:border-box;margin:0;padding:0}
html,body{width:1200px;height:2874px;overflow:hidden;background:var(--paper)}
body{position:relative;font-family:"Questrial",sans-serif;color:var(--text)}
.abs{position:absolute}
.caps{text-transform:uppercase;letter-spacing:2px}

/* header */
.site-header{left:0;top:0;width:1200px;height:80px;background:var(--paper)}
.brand{left:67px;top:26px;display:flex;align-items:center;gap:8px;font-family:"Jost",sans-serif;font-weight:500;font-size:24px;color:var(--ink)}
.brand-dot{width:26px;height:26px;border-radius:50%;background:#9a9a9a}
.main-nav{top:33px;font-size:11px;color:#777;font-family:"Jost",sans-serif}
.main-nav .home{color:var(--ink)}
.contact-btn{left:1016px;top:25px;width:120px;height:31px;border:1.5px solid #aaa;font-family:"Jost",sans-serif;font-weight:600;font-size:11px;letter-spacing:2px;display:flex;align-items:center;justify-content:center;color:var(--ink)}

/* hero */
.hero{left:0;top:80px;width:1200px;height:520px;background:linear-gradient(100deg,#5a4a40 0%,#8a7a6c 35%,#b8b2aa 60%,#8d9297 85%,#6e7378 100%)}
.hero-title{left:168px;top:210px;font-family:"Jost",sans-serif;font-weight:600;font-size:49px;line-height:59px;color:#fff;letter-spacing:1px}
.hero-sub{left:168px;top:352px;font-size:16px;line-height:26px;color:#fff}
.hero-sub b{font-weight:700}

/* opt-in */
.optin{left:168px;top:540px;width:400px;height:232px;background:var(--ink);box-shadow:0 14px 30px rgba(0,0,0,.18)}
.field{left:40px;width:320px;height:40px;border:1px solid #888;color:#aaa;font-size:13px;padding:12px 15px}
.optin-btn{left:40px;top:152px;width:144px;height:39px;background:#fff;color:var(--ink);font-family:"Jost",sans-serif;font-weight:600;font-size:11px;letter-spacing:2px;display:flex;align-items:center;justify-content:center}

/* intro */
.intro-head{left:632px;top:682px;font-family:"Jost",sans-serif;font-size:24.5px;line-height:36px;letter-spacing:1.5px;color:var(--ink);text-transform:uppercase}
.intro-head strong{font-weight:600}
.intro-copy{left:632px;top:847px;width:410px;font-size:13.4px;line-height:22.5px;color:#888}

/* posts */
.posts{left:0;top:999px;width:1200px;height:919px;background:var(--soft)}
.posts-title{left:0;top:1056px;width:1200px;text-align:center;font-family:"Jost",sans-serif;font-weight:500;font-size:24px;letter-spacing:3px;color:var(--ink)}
.posts-sub{left:0;top:1099px;width:1200px;text-align:center;font-size:13.4px;color:#888}
.card{width:335px}
.card-photo{width:335px;height:199px}
.card-date{margin-top:22px;font-family:"Jost",sans-serif;font-size:11px;letter-spacing:2.5px;color:#666;font-weight:500}
.card-title{margin-top:12px;font-family:"Jost",sans-serif;font-weight:500;font-size:16px;line-height:24px;letter-spacing:.8px;color:var(--ink)}
.card-title.active{text-decoration:underline}
.card.lifted .card-photo{box-shadow:0 10px 24px rgba(0,0,0,.18)}

.pager{left:65px;top:1807px;width:1071px;height:48px;background:#fff;font-family:"Jost",sans-serif;font-size:11px;color:#999;letter-spacing:2px}
.pager-prev{left:24px;top:17px}
.pager-next{right:24px;top:17px}
.pager-pages{left:458px;top:13px;display:flex;gap:8px}
.pager-pages span{width:24px;height:24px;border-radius:50%;background:#eeeeee;font-size:9px;letter-spacing:0;color:#333;display:flex;align-items:center;justify-content:center}

/* products */
.product-head{font-family:"Jost",sans-serif;font-weight:500;font-size:25px;line-height:36px;letter-spacing:2.5px;color:var(--ink)}
.product-copy{font-size:13.4px;line-height:22.5px;color:#888;width:380px}
.outline-btn{width:144px;height:32px;border:1.5px solid #aaa;font-family:"Jost",sans-serif;font-weight:600;font-size:11px;letter-spacing:2.5px;display:flex;align-items:center;justify-content:center;color:var(--ink)}
.placeholder{width:400px;height:280px;background:var(--placeholder)}

/* footer */
.site-footer{left:0;top:2673px;width:1200px;height:120px;background:var(--ink)}
.footer-links{left:168px;top:40px;font-family:"Jost",sans-serif;font-size:11.5px;letter-spacing:2px;color:#aaa}
.footer-copy{left:168px;top:70px;font-family:"Jost",sans-serif;font-size:11px;letter-spacing:2px;color:#888}
.social{top:40px;width:40px;height:40px;border:1.5px solid #777;border-radius:50%}
.signup-band{left:0;top:2793px;width:1200px;height:81px;background:var(--band)}
.signup-field{left:168px;top:20px;width:648px;height:40px;border-top:1px solid #555;border-bottom:1px solid #555;padding:12px 0 0 58px;font-size:13.4px;color:#222}
.signup-btn{left:833px;top:19px;width:198px;height:40px;background:var(--ink);color:#fff;font-family:"Jost",sans-serif;font-weight:600;font-size:11px;letter-spacing:2.5px;display:flex;align-items:center;justify-content:center}
</style>
</head>
<body>

<header class="site-header abs">
  <div class="brand abs"><span class="brand-dot"></span>Lumbero</div>
  <nav class="main-nav caps">
    <span class="abs home" style="left:405px">Home</span>
    <span class="abs" style="left:479px">CPM Questions</span>
    <span class="abs" style="left:626px">Resources</span>
    <span class="abs" style="left:742px">Notes</span>
    <span class="abs" style="left:819px">Resources</span>
    <span class="abs" style="left:934px">Ebook</span>
  </nav>
  <div class="contact-btn abs">CONTACT</div>
</header>

<section class="hero abs" role="img" aria-label="Photo of a smiling student with glasses working on a laptop"></section>
<h1 class="hero-title abs">NEVER MISS<br>A POST</h1>
<p class="hero-sub abs">Boost Your Skills. <b>Join 20,000+</b> Subscribers.<br>Download our <b>free guide!</b></p>

<form class="optin abs">
  <div class="field abs" style="top:40px">Your Name</div>
  <div class="field abs" style="top:96px">Email</div>
  <div class="optin-btn abs">GET IT NOW!</div>
</form>

<h2 class="intro-head abs">In the online marketing<br>space, everybody loves the<br>quick win. The shortcut.<br><strong>The "growth hack".</strong></h2>
<p class="intro-copy abs">Lorem ipsum dolor sit amet, consectetur adipiscing elit, sed do eiusmod tempor incididunt ut labore et dolore magna aliqua. Ut enim ad minim veniam,</p>

<section class="posts abs"></section>
<h2 class="posts-title abs">LATEST POSTS...</h2>
<p class="posts-sub abs">Prepare for CPM exams with on of oldest site with good enough topics.</p>

<article class="card lifted abs" style="left:65px;top:1152px">
  <div class="card-photo" role="img" aria-label="Photo of a teacher standing in a library with students" style="background:linear-gradient(120deg,#b9a68c,#e4ddd3 60%,#c9c6c2)"></div>
  <div class="card-date">APR 11, 2020</div>
  <h3 class="card-title active">The CPM Exam Lessons Learned By<br>Mira Kessland</h3>
</article>
<article class="card abs" style="left:433px;top:1152px">
  <div class="card-photo" role="img" aria-label="Photo of a lecturer addressing a classroom" style="background:linear-gradient(120deg,#d9c9b8,#bfa48e 55%,#a89886)"></div>
  <div class="card-date">JAN 25, 2020</div>
  <h3 class="card-title">The CPM Exam Lessons Learned By<br>Tomas Verhagen</h3>
</article>
<article class="card abs" style="left:801px;top:1152px">
  <div class="card-photo" role="img" aria-label="Photo of colleagues gathered around a laptop in an office" style="background:linear-gradient(120deg,#9aa3ab,#5a79b8 50%,#b9a9c2)"></div>
  <div class="card-date">NOV 19, 2019</div>
  <h3 class="card-title">The CPM Exam Lessons Learned By<br>Lena R Ostrova</h3>
</article>

<article class="card abs" style="left:65px;top:1480px">
  <div class="card-photo" role="img" aria-label="Photo of a tutor helping a student write at a desk" style="background:linear-gradient(120deg,#c8c2ba,#9c948b 50%,#c5ccd4)"></div>
  <div class="card-date">MAR 4, 2020</div>
  <h3 class="card-title">CPM-RX Exam Lessons Learned<br>By Idris Halloway</h3>
</article>
<article class="card abs" style="left:433px;top:1480px">
  <div class="card-photo" role="img" aria-label="Photo of students studying together at a table" style="background:linear-gradient(120deg,#8a5a48,#b9786a 50%,#6d6a80)"></div>
  <div class="card-date">MAR 4, 2020</div>
  <h3 class="card-title">CPM Exam Lessons Learned<br>By Noel Brandt</h3>
</article>
<article class="card abs" style="left:801px;top:1480px">
  <div class="card-photo" role="img" aria-label="Photo of an exam prep book on a blue background" style="background:linear-gradient(135deg,#2f7aa0,#3a87ad 50%,#2c6f94)"></div>
  <div class="card-date">MAR 4, 2020</div>
  <h3 class="card-title">The EVX Guide for the CPM Certification<br>Exam: Version 2.0</h3>
</article>

<nav class="pager abs" aria-label="Pagination">
  <span class="pager-prev abs">&larr;&nbsp;&nbsp;&nbsp;PREV</span>
  <div class="pager-pages abs"><span>1</span><span>2</span><span>3</span><span>···</span><span>12</span></div>
  <span class="pager-next abs">NEXT&nbsp;&nbsp;&nbsp;&rarr;</span>
</nav>

<section class="product">
  <h2 class="product-head abs" style="left:168px;top:2006px">THE CPM TRAINING<br>PROGRAM</h2>
  <p class="product-copy abs" style="left:168px;top:2099px">Sed ut perspiciatis unde omnis iste natus voluptatem accusantium doloremque laudantium, totam<br>rem aperiam, eaque ipsa quae ab.</p>
  <div class="outline-btn abs" style="left:168px;top:2199px">EXPLORE ALL</div>
  <svg class="placeholder abs" style="left:632px;top:1982px" viewBox="0 0 400 280" aria-label="Image placeholder">
    <g stroke="var(--placeholder-mark)" stroke-width="1.5" fill="none">
      <path d="M97 37l30 30M303 37l-30 30M97 243l30-30M303 243l-30-30"/>
      <rect x="152" y="98" width="96" height="84" stroke-width="6"/>
    </g>
    <circle cx="213" cy="120" r="9" fill="var(--placeholder-mark)"/>
    <path d="M158 176l30-36 22 22 14-12 20 26z" fill="var(--placeholder-mark)"/>
  </svg>
</section>

<section class="product">
  <svg class="placeholder abs" style="left:168px;top:2327px" viewBox="0 0 400 280" aria-label="Image placeholder">
    <g stroke="var(--placeholder-mark)" stroke-width="1.5" fill="none">
      <path d="M97 37l30 30M303 37l-30 30M97 243l30-30M303 243l-30-30"/>
      <rect x="152" y="98" width="96" height="84" stroke-width="6"/>
    </g>
    <circle cx="188" cy="120" r="9" fill="var(--placeholder-mark)"/>
    <path d="M158 176l30-36 22 22 14-12 20 26z" fill="var(--placeholder-mark)"/>
  </svg>
  <h2 class="product-head abs" style="left:632px;top:2350px">THE CPM EXAM<br>PREPARATION TOOL</h2>
  <p class="product-copy abs" style="left:632px;top:2443px">Sed ut perspiciatis unde omnis iste natus voluptatem accusantium doloremque laudantium, totam<br>rem aperiam, eaque ipsa quae ab.</p>
  <div class="outline-btn abs" style="left:632px;top:2543px">EXPLORE ALL</div>
</section>

<footer class="site-footer abs">
  <div class="footer-links abs">CPM QUESTIONS &nbsp;I&nbsp; RESOURCES &nbsp;I&nbsp; NOTES &nbsp;I&nbsp; RESOURCES &nbsp;I&nbsp; EBOOK &nbsp;I&nbsp; CONTACT</div>
  <div class="footer-copy abs">© 2019 LUMBERO.</div>
  <span class="social abs" style="left:852px" aria-label="Social profile"></span>
  <span class="social abs" style="left:900px" aria-label="Social profile"></span>
  <span class="social abs" style="left:948px" aria-label="Social profile"></span>
  <span class="social abs" style="left:996px" aria-label="Social profile"></span>
</footer>

<section class="signup-band abs">
  <svg class="abs" style="left:168px;top:22px" width="42" height="36" viewBox="0 0 42 36" aria-hidden="true">
    <g fill="none" stroke="#2a2a2a" stroke-width="1.4">
      <path d="M2 18L22 2l18 16-18 16z"/>
      <path d="M12 10l10 8 10-8"/>
    </g>
  </svg>
  <div class="signup-field abs">It all starts with one simple action. Drop your email.</div>
  <div class="signup-btn abs">SUBSCRIBE NOW!</div>
</section>

</body>
</html>
```